Brantley Studios photography and video creator

I need a business card for my production company. I shoot photography and videography for real estate, adventure sports and businesses

Contact Information for Business Card

simple not to busy

Colors

Designer to choose colors to be used in the design.

Requirements
Must have
• derek@brantleystudios.ca
• phone -5873304127
• instagram derek_brantley

```html
<!DOCTYPE html>
<html lang="en">
<head>
<meta charset="utf-8">
<title>Brantley Studios – Business Card</title>
<link href="https://fonts.googleapis.com/css2?family=Montserrat:wght@500;600&display=swap" rel="stylesheet">
<style>
  :root{
    --backdrop:#d9d4cc;
    --card-white:#f7f7f7;
    --card-black:#0c0c0c;
    --ink:#1c1c1c;
    --mist-light:#d2d2d2;
    --mist-mid:#8a8a8a;
    --mist-dark:#3a3a3a;
    --ring:#7c7c7c;
    --ring-gap:#b9b9b9;
    --mark-fill:#4a4a4a;
    --white:#ffffff;
  }
  *{margin:0;padding:0;box-sizing:border-box}
  html,body{width:1200px;height:720px;overflow:hidden}
  body{background:var(--backdrop);font-family:"Montserrat",Arial,sans-serif;position:relative}
  .card{position:absolute;top:241px;width:418px;height:239px;border-radius:11px;overflow:hidden}
  .card-front{left:148px;background:var(--card-white)}
  .card-back{left:634px;background:var(--card-black)}
  .card-art{position:absolute;inset:0}
  .brand-mark{position:absolute;left:47px;top:24px;width:76px;height:76px;border-radius:50%;background:var(--mark-fill)}
  .brand-name-front{position:absolute;left:20px;top:106px;width:130px;text-align:center;font-size:10px;font-weight:600;letter-spacing:1.5px;color:var(--ink)}
  .person-name{position:absolute;left:28px;top:140px;font-size:16px;font-weight:500;letter-spacing:.3px;color:var(--ink)}
  .contact-list{position:absolute;left:28px;top:171px;list-style:none;font-size:11.5px;font-weight:500;color:var(--ink)}
  .contact-list li{display:flex;align-items:center;height:17px}
  .contact-icon{width:12px;height:12px;margin-right:8px;flex:none}
  .social-square{width:10px;height:10px;margin:0 9px 0 1px;background:var(--ink);border-radius:2px;flex:none}
  .back-mark{position:absolute;left:187px;top:49px;width:150px;height:150px;border-radius:50%;background:var(--mist-dark)}
  .brand-name-back{position:absolute;left:162px;top:134px;width:200px;text-align:center;color:var(--white);font-weight:600}
  .brand-name-back .line-main{display:block;font-size:23px;letter-spacing:1px;line-height:1}
  .brand-name-back .line-sub{display:block;font-size:7px;letter-spacing:3px;margin-top:4px}
</style>
</head>
<body>

<section class="card card-front">
  <svg class="card-art" width="418" height="239" viewBox="0 0 418 239">
    <defs>
      <linearGradient id="landscape-front" x1="0" y1="0" x2="0" y2="1">
        <stop offset="0" stop-color="#e6e6e6"/>
        <stop offset=".35" stop-color="#9a9a9a"/>
        <stop offset="1" stop-color="#2e2e2e"/>
      </linearGradient>
    </defs>
    <circle cx="402" cy="128" r="142" fill="var(--ring)"/>
    <circle cx="414" cy="128" r="134" fill="var(--ring-gap)"/>
    <circle cx="425" cy="130" r="126" fill="url(#landscape-front)" role="img" aria-label="Mountain ridges and pine tree landscape in greyscale"/>
  </svg>

  <div class="brand-mark"></div>
  <div class="brand-name-front">BRANTLEY STUDIOS</div>

  <h1 class="person-name">DEREK BRANTLEY</h1>
  <ul class="contact-list">
    <li>
      <svg class="contact-icon" viewBox="0 0 24 24"><path fill="var(--ink)" d="M6.6 10.8a15.1 15.1 0 0 0 6.6 6.6l2.2-2.2a1 1 0 0 1 1-.25 11.4 11.4 0 0 0 3.6.57 1 1 0 0 1 1 1V20a1 1 0 0 1-1 1A17 17 0 0 1 3 4a1 1 0 0 1 1-1h3.5a1 1 0 0 1 1 1c0 1.25.2 2.45.57 3.57a1 1 0 0 1-.25 1z"/></svg>
      5873 304 127
    </li>
    <li>
      <svg class="contact-icon" viewBox="0 0 24 24"><rect x="2" y="5" width="20" height="14" rx="1" fill="var(--ink)"/><path d="M3 6l9 7 9-7" fill="none" stroke="var(--card-white)" stroke-width="1.6"/></svg>
      derek@brantleystudios.ca
    </li>
    <li>
      <span class="social-square"></span>
      instagram derek_brantley
    </li>
  </ul>
</section>

<section class="card card-back">
  <svg class="card-art" width="418" height="239" viewBox="0 0 418 239">
    <defs>
      <linearGradient id="landscape-back" x1="0" y1="0" x2="0" y2="1">
        <stop offset="0" stop-color="#f0f0f0"/>
        <stop offset=".5" stop-color="#8c8c8c"/>
        <stop offset="1" stop-color="#2a2a2a"/>
      </linearGradient>
    </defs>
    <circle cx="300" cy="-10" r="120" fill="#141414"/>
    <circle cx="130" cy="200" r="110" fill="#161616"/>
    <circle cx="330" cy="230" r="90" fill="#121212"/>
    <circle cx="0" cy="118" r="104" fill="url(#landscape-back)" role="img" aria-label="Pine tree before misty mountain ridges in greyscale"/>
  </svg>
  <div class="back-mark"></div>
  <div class="brand-name-back">
    <span class="line-main">BRANTLEY</span>
    <span class="line-sub">STUDIOS</span>
  </div>
</section>

</body>
</html>
```